Biz Card for Harrowfield Property Partners - HFPP

Harrowfield Property Partners is a commercial real estate acquisitions firm. We buy commercial property and need to raise capital from investors for each deal we buy. The vibe needs to be: give us your money, we will multiply it.
Our website: www.hfldpp.com
Competitors are: https://marvenby.com/, https://trellumpartners.com/, http://www.quorvantcapital.com/
Target Market(s)
High Net Worth Individuals, Bankers, Insurance Companies, Commercial Real Estate Brokers.
Industry/Entity Type
Investment Banking
Contact Information for Business Card
Name, Title, Addess, Cell#, Office#, email, website
Requirements
Must have
- use one of our logos. See website for look and feel: www.hfldpp.com
Nice to have
- see website: www.hfldpp.com

```html
<!DOCTYPE html>
<html lang="en">
<head>
<meta charset="utf-8">
<title>Harrowfield Property Partners – Business Card</title>
<link href="https://fonts.googleapis.com/css2?family=Montserrat:wght@400;500;700&display=swap" rel="stylesheet">
<style>
  :root {
    --navy: #062641;
    --paper: #ffffff;
    --stage: #e9ecef;
    --ink: #0a2a45;
  }
  * { box-sizing: border-box; margin: 0; padding: 0; }
  html, body { width: 1200px; height: 1200px; overflow: hidden; }
  body {
    background: var(--stage);
    font-family: "Montserrat", sans-serif;
    position: relative;
  }
  .card {
    position: absolute;
    left: 150px;
    width: 900px;
    height: 514px;
    box-shadow: 0 6px 18px rgba(0,0,0,0.18);
    overflow: hidden;
  }
  .card--front { top: 66px; background: var(--navy); color: var(--paper); }
  .card--back { top: 620px; background: var(--paper); color: var(--ink); }

  /* front */
  .front-brand {
    position: absolute;
    left: 330px; top: 110px;
    width: 480px;
    text-align: center;
  }
  .brand-dot {
    display: block;
    margin: 0 auto 22px;
    width: 120px; height: 120px;
    border-radius: 50%;
    background: var(--paper);
  }
  .brand-name {
    font-weight: 500;
    color: var(--paper);
    line-height: 1.1;
  }
  .brand-name__main { display: block; font-size: 40px; letter-spacing: 6px; }
  .brand-name__sub { display: block; font-size: 17px; letter-spacing: 7px; margin-top: 8px; }
  .front-url {
    margin-top: 38px;
    font-size: 20px;
    letter-spacing: 9px;
    color: var(--paper);
  }

  /* back */
  .back-brand {
    position: absolute;
    left: 40px; top: 80px;
    width: 400px;
    text-align: center;
  }
  .back-brand .brand-dot { background: var(--navy); width: 130px; height: 130px; }
  .back-brand .brand-name { color: var(--ink); }
  .back-brand .brand-name__main { font-size: 38px; letter-spacing: 5px; }
  .back-brand .brand-name__sub { font-size: 16px; letter-spacing: 6px; }

  .divider {
    position: absolute;
    left: 478px; top: 58px;
    width: 2px; height: 290px;
    background: var(--ink);
  }
  .contact {
    position: absolute;
    left: 520px; top: 70px;
    width: 360px;
  }
  .contact__name { font-size: 27px; font-weight: 700; letter-spacing: 0.5px; }
  .contact__title { font-size: 19px; font-weight: 500; margin-top: 2px; }
  .contact__address { font-size: 19px; font-weight: 500; margin-top: 22px; line-height: 1.25; }
  .contact__list { list-style: none; margin-top: 12px; }
  .contact__item {
    display: flex; align-items: center; gap: 12px;
    font-size: 21px; font-weight: 500; line-height: 1.5;
  }
  .contact__icon { width: 22px; height: 22px; flex: none; }

  .url-band {
    position: absolute;
    left: 0; top: 404px;
    width: 100%; height: 64px;
    background: var(--navy);
    color: var(--paper);
    display: flex; align-items: center; justify-content: center;
    font-size: 22px; font-weight: 500; letter-spacing: 9px;
    padding-right: 180px;
  }
</style>
</head>
<body>

<section class="card card--front" aria-label="Card front">
  <div class="front-brand">
    <span class="brand-dot" aria-hidden="true"></span>
    <div class="brand-name">
      <span class="brand-name__main">HARROWFIELD</span>
      <span class="brand-name__sub">PROPERTY PARTNERS</span>
    </div>
    <p class="front-url">www.hfldpp.com</p>
  </div>
</section>

<section class="card card--back" aria-label="Card back">
  <div class="back-brand">
    <span class="brand-dot" aria-hidden="true"></span>
    <div class="brand-name">
      <span class="brand-name__main">HARROWFIELD</span>
      <span class="brand-name__sub">PROPERTY PARTNERS</span>
    </div>
  </div>

  <div class="divider" aria-hidden="true"></div>

  <div class="contact">
    <p class="contact__name">CORWIN L. ASHBY</p>
    <p class="contact__title">Executive Director</p>
    <p class="contact__address">PO BOX 418 Calder Court<br>74 Wrenfield Ave, USA</p>
    <ul class="contact__list">
      <li class="contact__item">
        <svg class="contact__icon" viewBox="0 0 24 24" aria-hidden="true">
          <circle cx="12" cy="12" r="11" fill="none" stroke="var(--ink)" stroke-width="2"/>
          <path d="M8.5 6.5l2 2-1.2 1.5c.7 1.6 2 2.9 3.7 3.7l1.5-1.2 2 2-1.3 1.8c-3.8-.5-7.2-3.9-7.7-7.7z" fill="var(--ink)"/>
        </svg>
        555-014-2270
      </li>
      <li class="contact__item">
        <svg class="contact__icon" viewBox="0 0 24 24" aria-hidden="true">
          <circle cx="12" cy="12" r="11" fill="none" stroke="var(--ink)" stroke-width="2"/>
          <rect x="7" y="7" width="10" height="10" rx="1.5" fill="none" stroke="var(--ink)" stroke-width="2"/>
        </svg>
        555-014-2281
      </li>
      <li class="contact__item">
        <svg class="contact__icon" viewBox="0 0 24 24" aria-hidden="true">
          <circle cx="12" cy="12" r="11" fill="none" stroke="var(--ink)" stroke-width="2"/>
          <rect x="6.5" y="8" width="11" height="8" fill="none" stroke="var(--ink)" stroke-width="1.6"/>
          <path d="M6.5 8l5.5 4.5L17.5 8" fill="none" stroke="var(--ink)" stroke-width="1.6"/>
        </svg>
        info@hfldpp.com
      </li>
    </ul>
  </div>

  <div class="url-band">www.hfldpp.com</div>
</section>

</body>
</html>
```